The Maplewood Kids Health Centre needs a Letterhead

We are a bilingual pediatric clinic located in Montreal, Canada.

Our english name is Maplewood Kids Health Centre
Our french name is Centre médical Bellerive

We offer complete care for children including general pediatric care, pediatric specialist care such as Ear, Nose and Throat, Urology, Neurology and Adolescent Medicine. We also have paramedical specialists such as psychologists, social workers, occupational therapists, speech and language pathologists.

The letterhead must use and be harmonious with our new logo. See Design #4923293. We need two types of letterhead. One for a the Logo and both english and french names on the top and the second with the list of current staff on the left. I have uploaded two old examples for you to see. Thanks and good luck.

Industry/Entity Type

Clinic

Font styles to use
Sans Serif

Colors
3176b5
9d9d9d

Requirements
Must have
• Include our logo.
Nice to have
• Most of our printing is done in black and white. So a grayscale design is fine.
I have included a color and grayscale versions of our logo.

We prefer clean modern designs.

```html
<!DOCTYPE html>
<html lang="en">
<head>
<meta charset="utf-8">
<title>Maplewood Kids Health Centre – Letterhead</title>
<link rel="stylesheet" href="https://fonts.googleapis.com/css2?family=Open+Sans:wght@400;600;700&family=Arimo:wght@400&display=swap">
<style>
  :root {
    --ink-purple: #5b4a86;
    --ink-blue: #3176b5;
    --rule-teal: #3f86a6;
    --brand-blue: #5f72b6;
    --band-purple: #5b4a7a;
    --band-blue: #6570b0;
    --icon-grey: #9d9d9d;
    --paper: #ffffff;
  }
  * { margin: 0; padding: 0; box-sizing: border-box; }
  html, body { width: 848px; height: 1200px; overflow: hidden; background: var(--paper); }
  .letterhead {
    position: relative;
    width: 848px;
    height: 1200px;
    background: var(--paper);
    font-family: "Open Sans", Arial, sans-serif;
  }
  .address {
    position: absolute;
    left: 47px;
    top: 36px;
    font-size: 10.5px;
    line-height: 15.5px;
    color: var(--ink-purple);
  }
  .address .label { color: var(--ink-blue); font-weight: 700; }
  .address .gap { display: inline-block; width: 16px; }
  .header-icons {
    position: absolute;
    left: 328px;
    top: 42px;
    width: 158px;
    height: 44px;
    border-radius: 6px;
    background: linear-gradient(90deg, #eeeeee, #f6f6f6);
  }
  .brand {
    position: absolute;
    left: 580px;
    top: 32px;
    width: 228px;
    height: 62px;
    display: flex;
    align-items: center;
    justify-content: space-between;
    font-family: "Arimo", Arial, sans-serif;
    font-size: 15px;
    line-height: 16px;
    color: var(--brand-blue);
  }
  .brand-fr { text-align: right; width: 80px; }
  .brand-en { text-align: left; width: 92px; }
  .brand-dot {
    width: 34px; height: 34px; border-radius: 50%;
    background: var(--brand-blue);
    flex: none;
  }
  .header-rule {
    position: absolute;
    left: 0; top: 103px;
    width: 848px; height: 3px;
    background: var(--rule-teal);
  }
  .staff-footer {
    position: absolute;
    left: 0; top: 1141px;
    width: 848px; height: 59px;
    background: var(--band-blue);
  }
  .staff-footer::before {
    content: "";
    position: absolute;
    left: 0; top: 0;
    width: 848px; height: 12px;
    background: var(--band-purple);
  }
  .staff-group {
    position: absolute;
    top: 0;
    color: #ffffff;
    font-size: 6.2px;
  }
  .staff-group h3 {
    height: 12px;
    line-height: 12px;
    font-weight: 700;
    font-size: 6.2px;
    white-space: nowrap;
  }
  .staff-list {
    list-style: none;
    display: grid;
    grid-auto-flow: column;
    grid-template-rows: repeat(4, 7.6px);
    column-gap: 10px;
    margin-top: 3px;
    margin-left: 4px;
  }
  .staff-list li { white-space: nowrap; line-height: 7.6px; font-size: 5.4px; opacity: .9; }
  .staff-list li::before { content: "• "; }
</style>
</head>
<body>
<div class="letterhead">
  <header>
    <p class="address">
      2250 rue des Érables,<br>
      Suite 210, Montréal, Qc, H3X 2K7<br>
      <span class="label">tel:</span> (514) 555-0148<span class="gap"></span><span class="label">fax:</span> (514) 555-0192
    </p>
    <div class="header-icons" role="img" aria-label="Hand-drawn doodles of a child, a heart and a house"></div>
    <div class="brand">
      <span class="brand-fr">Centre médical Bellerive</span>
      <span class="brand-dot"></span>
      <span class="brand-en">Maplewood Kids Health Centre</span>
    </div>
    <div class="header-rule"></div>
  </header>

  <footer class="staff-footer">
    <div class="staff-group" style="left:50px">
      <h3>Pédiatres / Pediatricians</h3>
      <ul class="staff-list">
        <li>M. Tremblay</li><li>J. Gagnon</li><li>L. Bouchard</li><li>S. Côté</li>
        <li>A. Pelletier</li><li>R. Lavoie</li><li>C. Morin</li>
      </ul>
    </div>
    <div class="staff-group" style="left:154px">
      <h3>Neurologue / Neurologist</h3>
      <ul class="staff-list" style="margin-left:22px"><li>N. Fortin</li></ul>
    </div>
    <div class="staff-group" style="left:252px">
      <h3>O.R.L. / E.N.T.</h3>
      <ul class="staff-list" style="margin-left:10px"><li>P. Girard</li></ul>
    </div>
    <div class="staff-group" style="left:326px">
      <h3>Urologue / Urologist</h3>
      <ul class="staff-list" style="margin-left:16px"><li>D. Caron</li></ul>
    </div>
    <div class="staff-group" style="left:418px">
      <h3>Psychologues / Psychologists</h3>
      <ul class="staff-list" style="margin-left:24px"><li>H. Bélanger</li><li>V. Roy</li></ul>
    </div>
    <div class="staff-group" style="left:533px">
      <h3>Travailleuse social / Social worker</h3>
      <ul class="staff-list" style="margin-left:36px"><li>E. Lévesque</li></ul>
    </div>
    <div class="staff-group" style="left:658px">
      <h3>Diététiste / Dietician</h3>
      <ul class="staff-list" style="margin-left:18px"><li>I. Poirier</li></ul>
    </div>
    <div class="staff-group" style="left:744px">
      <h3>Gerante / Manager</h3>
      <ul class="staff-list" style="margin-left:16px"><li>K. Simard</li></ul>
    </div>
  </footer>
</div>
</body>
</html>
```